Handmade Soap Labels Needed for Local Soap Supplier

I am rebranding my Handmade Soap Business and require New Handmade Soap Labels. I made the current labels on word and they need a fresh new look for the new business name. I live in Seabrook, Southern Coast and the culture is very environmentally friendly and supports local products. The final design would need to be simple but eye catching. There are 16 soap varieties at the moment so I would need to be able to edit the labels to update ingredients etc for new soap varieties. I have attached my current label for you to see what I currently have. The business name is also changing so I have included the new logo which is needed on the new labels.

Requirements
Must have
• Must have logo, name of the soap eg. Lavender
• Soap ingredients
• Handmade
Nice to have
• Design that is eye catching and would make a great gift
Should not have
• Should not be too busy

```html
<!DOCTYPE html>
<html lang="en">
<head>
<meta charset="utf-8">
<title>Bramble &amp; Birch Soap Co – Lavender Labels</title>
<link rel="stylesheet" href="https://fonts.googleapis.com/css2?family=Sorts+Mill+Goudy&family=Roboto+Condensed:wght@300;400&family=Josefin+Sans:wght@300;400&display=swap">
<style>
  :root {
    --teal: #8ac6c5;
    --ink: #4a4a4a;
    --soft-ink: #666;
    --paper: #ffffff;
    --heart: #d9262b;
    --serif: "Sorts Mill Goudy", Georgia, serif;
    --sans: "Josefin Sans", Arial, sans-serif;
    --cond: "Roboto Condensed", "Arial Narrow", sans-serif;
  }
  * { margin: 0; padding: 0; box-sizing: border-box; }
  html, body { width: 1200px; height: 1000px; overflow: hidden; background: var(--paper); }
  .canvas { position: relative; width: 1200px; height: 1000px; }
  .band { position: absolute; background: var(--teal); }

  /* brand name */
  .brand { position: absolute; text-align: center; font-family: var(--serif); color: var(--ink); white-space: nowrap; }
  .brand--front { left: 400px; width: 400px; top: 120px; font-size: 36px; }
  .brand--wrap { left: 457px; width: 300px; top: 556px; font-size: 22px; }

  /* teal panel */
  .panel { position: absolute; background: var(--teal); color: var(--paper); text-align: center; }
  .panel--front { left: 307px; top: 224px; width: 586px; height: 230px; border-radius: 30px 30px 0 0; }
  .panel--wrap { left: 434px; top: 613px; width: 346px; height: 140px; border-radius: 22px 22px 0 0; }

  .kicker { position: absolute; left: 0; right: 0; display: flex; align-items: center; justify-content: center; font-family: var(--sans); font-weight: 300; }
  .kicker::before, .kicker::after { content: ""; height: 1.5px; background: var(--paper); flex: 1; }
  .kicker span { padding: 0 10px; }
  .panel--front .kicker { top: 14px; left: 67px; right: 67px; font-size: 23px; }
  .panel--wrap .kicker { top: 8px; left: 40px; right: 40px; font-size: 14px; }

  .soap-name { position: absolute; left: 0; right: 0; font-family: var(--serif); }
  .panel--front .soap-name { top: 40px; font-size: 61px; }
  .panel--wrap .soap-name { top: 26px; font-size: 35px; }

  .rule { position: absolute; height: 1.5px; background: var(--paper); }
  .panel--front .rule { top: 123px; left: 67px; right: 67px; }
  .panel--wrap .rule { top: 73px; left: 40px; right: 40px; }

  .sprig { position: absolute; background: rgba(255,255,255,0.85); border-radius: 40% 60% 40% 60%; }
  .panel--front .sprig { top: 50px; width: 50px; height: 38px; }
  .panel--front .sprig--l { left: 40px; } .panel--front .sprig--r { right: 40px; }
  .panel--wrap .sprig { top: 30px; width: 28px; height: 22px; }
  .panel--wrap .sprig--l { left: 24px; } .panel--wrap .sprig--r { right: 24px; }

  .love { position: absolute; left: 0; right: 0; font-family: var(--cond); font-weight: 300; line-height: 1; }
  .love__top { display: inline-block; border-bottom: 1.5px dotted var(--paper); letter-spacing: 0.5px; }
  .love__bottom { display: flex; align-items: center; justify-content: center; gap: 6px; }
  .heart { display: inline-block; }
  .panel--front .love { top: 150px; }
  .panel--front .love__top { font-size: 33px; padding-bottom: 2px; }
  .panel--front .love__bottom { font-size: 25px; margin-top: 2px; gap: 10px; }
  .panel--wrap .love { top: 88px; }
  .panel--wrap .love__top { font-size: 19px; padding-bottom: 1px; }
  .panel--wrap .love__bottom { font-size: 15px; margin-top: 1px; }

  /* wrap side panels */
  .divider { position: absolute; top: 542px; width: 1px; height: 190px; background: var(--teal); }

  .ingredients { position: absolute; left: 48px; top: 541px; width: 202px; text-align: center; color: var(--ink); }
  .ingredients__title { font-family: var(--cond); font-weight: 300; font-size: 23px; letter-spacing: 0.5px; display: flex; align-items: center; justify-content: center; gap: 6px; }
  .ingredients__title i { display: inline-block; width: 12px; height: 12px; background: var(--soft-ink); border-radius: 50% 0; }
  .ingredients__list { font-family: var(--serif); font-size: 14px; line-height: 19.5px; margin-top: 8px; }

  .vtext { position: absolute; top: 542px; height: 190px; writing-mode: vertical-rl; text-align: center; color: var(--ink); font-family: var(--cond); font-weight: 300; white-space: nowrap; }
  .vtext--up { transform: rotate(180deg); }
  .vtext--batches { left: 281px; font-size: 17px; letter-spacing: 1.5px; }
  .vtext--traditional { left: 343px; font-size: 16px; letter-spacing: 3px; line-height: 22px; }
  .vtext--lather { left: 815px; font-size: 13px; letter-spacing: 1.5px; line-height: 18px; }
  .vtext--process { left: 880px; font-size: 13.5px; line-height: 15px; letter-spacing: 0.3px; }
  .vtext--town { left: 962px; line-height: 20px; }
  .town__name { font-size: 16px; letter-spacing: 5px; }
  .town__region { font-size: 13px; letter-spacing: 0.5px; }
  .vtext--contact { left: 1027px; font-size: 12px; line-height: 16px; }
  .vtext--love { left: 1072px; font-size: 27px; line-height: 1; color: var(--ink); }
  .vtext--love .love__top { border-bottom: 0; border-left: 1.5px dotted var(--ink); padding-left: 2px; }
  .vtext--love .love__bottom { font-size: 20px; display: inline-flex; gap: 5px; }
</style>
</head>
<body>
<div class="canvas">

  <section class="label-front">
    <div class="band" style="left:282px;top:65px;width:636px;height:13px;"></div>
    <div class="brand brand--front">Bramble &amp; Birch Soap Co</div>
    <div class="panel panel--front">
      <div class="kicker"><span>Handmade Soap</span></div>
      <div class="sprig sprig--l" role="img" aria-label="Small leaf sprig ornament"></div>
      <div class="soap-name">LAVENDER</div>
      <div class="sprig sprig--r" role="img" aria-label="Small leaf sprig ornament"></div>
      <div class="rule"></div>
      <div class="love">
        <span class="love__top">HANDMADE</span>
        <div class="love__bottom">WITH
          <svg class="heart" width="18" height="17" viewBox="0 0 20 18" aria-hidden="true"><path d="M10 18 L1.8 9.6 A5 5 0 0 1 10 3 A5 5 0 0 1 18.2 9.6 Z" fill="var(--heart)"/></svg>
          LOVE</div>
      </div>
    </div>
    <div class="band" style="left:282px;top:448px;width:636px;height:14px;"></div>
  </section>

  <section class="label-wrap">
    <div class="band" style="left:35px;top:520px;width:1143px;height:7px;"></div>
    <div class="band" style="left:35px;top:746px;width:1143px;height:7px;"></div>

    <div class="ingredients">
      <div class="ingredients__title"><i role="img" aria-label="Leaf ornament"></i>INGREDIENTS<i role="img" aria-label="Leaf ornament"></i></div>
      <p class="ingredients__list">Purified Water, Olive Oil,<br>Coconut Oil, Rice Bran Oil,<br>Sunflower Oil, Organic Shea<br>Butter, Sodium Hydroxide,</p>
    </div>

    <div class="divider" style="left:262px;"></div>
    <div class="vtext vtext--batches">SMALL BATCHES</div>
    <div class="vtext vtext--traditional">TRADITIONAL<br>HAND CRAFTED SOAP</div>
    <div class="divider" style="left:408px;"></div>

    <div class="brand brand--wrap">Bramble &amp; Birch Soap Co</div>
    <div class="panel panel--wrap">
      <div class="kicker"><span>Handmade Soap</span></div>
      <div class="sprig sprig--l" role="img" aria-label="Small leaf sprig ornament"></div>
      <div class="soap-name">LAVENDER</div>
      <div class="sprig sprig--r" role="img" aria-label="Small leaf sprig ornament"></div>
      <div class="rule"></div>
      <div class="love">
        <span class="love__top">HANDMADE</span>
        <div class="love__bottom">WITH
          <svg class="heart" width="12" height="11" viewBox="0 0 20 18" aria-hidden="true"><path d="M10 18 L1.8 9.6 A5 5 0 0 1 10 3 A5 5 0 0 1 18.2 9.6 Z" fill="var(--heart)"/></svg>
          LOVE</div>
      </div>
    </div>

    <div class="divider" style="left:806px;"></div>
    <div class="vtext vtext--up vtext--lather">RICH GENEROUS LATHER<br>100%&nbsp;&nbsp;SUSTAINABLE</div>
    <div class="vtext vtext--up vtext--process">EACH BATCH IS HAND MADE<br>IN MY KITCHEN, CUT BY HAND,<br>THEN CURED FOR 4 WEEKS<br>FOR YOU TO ENJOY.</div>
    <div class="divider" style="left:952px;"></div>
    <div class="vtext vtext--up vtext--town"><span class="town__name">SEABROOK</span><br><span class="town__region">SOUTHERN COAST</span></div>
    <div class="vtext vtext--up vtext--contact">0400 123 456<br>hello@brambleandbirch.com</div>
    <div class="vtext vtext--up vtext--love">
      <span class="love__top">HANDMADE</span><br>
      <span class="love__bottom">WITH
        <svg class="heart" width="15" height="14" viewBox="0 0 20 18" style="transform:rotate(90deg)" aria-hidden="true"><path d="M10 18 L1.8 9.6 A5 5 0 0 1 10 3 A5 5 0 0 1 18.2 9.6 Z" fill="var(--heart)"/></svg>
        LOVE</span>
    </div>
  </section>

</div>
</body>
</html>
```